Single Sided 1 Page Tour Flyer in the same theme as previous brochure

We need a single sided 8.5 x 11 flyer in the same theme and color scheme as the previous brochure we worked on together. the flyer should include the following

1. company logo up top (just like on the front panel of previous brochure
2. tour name "Maple & Pine Highlights" also on the top
3. a large photo towards the top of the flyer, similar to the brochure front
4. 3 panels of text: left one for tour prices, whats included, additional notes, center and right panels for tour program details (day 1, day 2, etc)
5. below that, a few lines for additional details, like small print and stuff
6. company address, phone numbers, email address, and website link
6. below that a banner of small photos, maybe 4 in a row, similar to the brochure

details of the actual tour can be found at this link:
http://bluepebbletrips.ru/en/tours/maple-and-pine-11-days/

once again, we would love for the flyer to be in the same theme and style as the other brochure, so it matches, we loved the previous work!!

```html
<!DOCTYPE html>
<html lang="en">
<head>
<meta charset="utf-8">
<title>Maple &amp; Pine Highlights – Tour Flyer</title>
<link rel="stylesheet" href="https://fonts.googleapis.com/css2?family=Exo+2:wght@500;600;700&family=Mulish:ital,wght@0,400;0,600;1,400&display=swap">
<style>
:root{
  --red:#c8161d;
  --red-dark:#8f0f14;
  --gold:#f2b705;
  --ink:#2b2b2b;
  --text:#3c3c3c;
  --grey:#4a4a4a;
  --paper:#ffffff;
  --mist:#ececec;
}
*{margin:0;padding:0;box-sizing:border-box}
html,body{width:949px;height:1200px;overflow:hidden;background:var(--paper)}
body{font-family:"Mulish",sans-serif;color:var(--text);position:relative}
.flyer{position:relative;width:949px;height:1200px;overflow:hidden;background:var(--paper)}
.header-art{position:absolute;left:0;top:0}
.brand{position:absolute;left:36px;top:70px;display:flex;align-items:center;gap:12px}
.brand-dot{width:34px;height:34px;border-radius:50%;background:var(--gold)}
.brand-name{font-family:"Exo 2",sans-serif;font-weight:600;font-size:34px;color:var(--ink);letter-spacing:-.3px}
.tour-title{position:absolute;right:37px;top:40px;font-family:"Exo 2",sans-serif;font-weight:700;font-size:33px;color:var(--ink)}
.section-title{position:absolute;left:32px;top:508px;display:flex;align-items:center;gap:8px;font-family:"Exo 2",sans-serif;font-weight:700;font-size:24px;color:var(--ink)}
.section-title .dot{width:11px;height:11px;border-radius:50%;background:var(--gold)}
.route{position:absolute;left:298px;top:522px;width:420px;font-family:"Exo 2",sans-serif;font-weight:600;font-size:17px;line-height:21px;color:var(--red)}
.price-badge{position:absolute;left:749px;top:484px;width:164px;height:100px;border-radius:50%;
  background:radial-gradient(ellipse at 50% 40%,#e0262d 0%,var(--red) 55%,var(--red-dark) 100%);
  box-shadow:0 0 0 3px #b01218 inset;color:#fff;text-align:center;padding-top:14px}
.price-badge .label{font-size:12.5px;line-height:16px}
.price-badge .amount{font-family:"Exo 2",sans-serif;font-weight:700;font-size:26px;color:var(--gold);line-height:32px}
.col{position:absolute;font-size:12.6px;line-height:16.3px}
.col-prices{left:32px;top:546px;width:278px}
.intro{font-size:13px;line-height:17px}
.intro em{font-style:italic}
.rates{display:flex;gap:28px;margin-top:18px}
.rate b{display:block;font-family:"Exo 2",sans-serif;font-weight:600;font-size:16px;color:var(--ink)}
.rate span{display:block;font-family:"Exo 2",sans-serif;font-weight:600;font-size:17px;color:var(--red);margin-top:5px}
.list-head{font-weight:600;color:var(--ink);margin-top:17px;font-size:13px}
.bullets{list-style:none;margin-top:3px}
.bullets li{position:relative;padding-left:9px;line-height:18px}
.bullets li::before{content:"";position:absolute;left:0;top:7px;width:5px;height:5px;border-radius:50%;background:var(--red)}
.note{font-style:italic;text-align:justify;margin-top:12px;line-height:15.5px}
.note + .note{margin-top:8px}
.col-days-a{left:344px;top:582px;width:266px}
.col-days-b{left:649px;top:582px;width:268px}
.day{text-align:justify;margin-bottom:14px}
.day h3{font-family:"Exo 2",sans-serif;font-weight:600;font-size:16px;color:var(--red);line-height:20px;margin-bottom:2px}
.day p{line-height:16.3px}
.day em{font-style:italic}
.fine{position:absolute;font-size:9.4px;line-height:11px;font-style:italic;color:#6a6a6a}
.fine-left{left:91px;top:1066px;width:440px}
.fine-left p + p{margin-top:6px}
.fine-right{left:554px;top:1066px;width:290px}
.footer-art{position:absolute;left:0;top:1065px}
.contact{position:absolute;color:#fff;display:flex;align-items:center;gap:6px}
.address{left:28px;top:1150px;font-size:14px;line-height:18px;align-items:flex-start}
.email{left:389px;top:1167px;font-size:17px}
.phone{left:684px;top:1140px;font-family:"Exo 2",sans-serif;font-weight:600;font-size:19px}
.web{left:660px;top:1167px;font-size:17px}
.contact svg{flex:none}
</style>
</head>
<body>
<main class="flyer">

  <svg class="header-art" width="949" height="520" viewBox="0 0 949 520" aria-hidden="false">
    <defs>
      <linearGradient id="sky" x1="0" y1="0" x2="0" y2="1">
        <stop offset="0" stop-color="#2f3470"/>
        <stop offset=".45" stop-color="#5c5394"/>
        <stop offset=".62" stop-color="#8a6a8e"/>
        <stop offset=".72" stop-color="#d0773a"/>
        <stop offset=".8" stop-color="#3b3f76"/>
        <stop offset="1" stop-color="#2c3464"/>
      </linearGradient>
      <linearGradient id="mist" x1="0" y1="0" x2="1" y2="0">
        <stop offset="0" stop-color="#ffffff"/>
        <stop offset="1" stop-color="#e6e6e6"/>
      </linearGradient>
    </defs>
    <path d="M230,0 H949 V170 C720,128 470,60 230,0Z" fill="url(#mist)"/>
    <path d="M0,168 C230,150 480,150 720,158 C480,160 240,172 0,196Z" fill="var(--gold)"/>
    <g role="img" aria-label="Photo: suspension bridge lit orange at dusk over a bay with city lights">
      <path d="M0,186 C300,166 620,150 949,176 V470 C700,478 420,500 0,482Z" fill="url(#sky)"/>
    </g>
    <path d="M560,480 C700,470 830,462 949,455 V492 C830,488 700,484 560,480Z" fill="var(--gold)"/>
    <g stroke="var(--red)" stroke-width="5">
      <ellipse role="img" aria-label="Photo: statue with torch against pale sky" cx="128" cy="245" rx="77" ry="40" fill="#a9b7b0"/>
      <ellipse role="img" aria-label="Photo: street signs at a busy city corner" cx="528" cy="245" rx="77" ry="40" fill="#7b8390"/>
      <ellipse role="img" aria-label="Photo: hotel facade lit at night" cx="694" cy="245" rx="77" ry="40" fill="#2f3452"/>
      <ellipse role="img" aria-label="Photo: tour boat below a large waterfall" cx="859" cy="245" rx="77" ry="40" fill="#8ea8b9"/>
    </g>
  </svg>

  <div class="brand">
    <span class="brand-dot"></span>
    <span class="brand-name">Blue Pebble Trips</span>
  </div>
  <h1 class="tour-title">Maple &amp; Pine Highlights</h1>

  <h2 class="section-title"><span class="dot"></span>Tour Itinerary<span class="dot"></span></h2>
  <p class="route">New York, Washington, D.C., Philadelphia, Boston, Montreal, Quebec, Ottawa, Niagara Falls</p>

  <div class="price-badge">
    <div class="label">Cost for<br>1 person from</div>
    <div class="amount">$1,495</div>
  </div>

  <section class="col col-prices">
    <p class="intro">The cost of tour for one person<br><em>(Personalize in process of purchasing)</em></p>
    <div class="rates">
      <div class="rate"><b>DBL</b><span>$1,495</span></div>
      <div class="rate"><b>SNGL</b><span>$1,995</span></div>
      <div class="rate"><b>TRPL</b><span>$1,395</span></div>
    </div>
    <p class="list-head">Included in Price:</p>
    <ul class="bullets">
      <li>Double occupancy in hotels along the route</li>
      <li>Breakfasts</li>
      <li>Excursions as per itinerary</li>
    </ul>
    <p class="list-head">Not Included in Price:</p>
    <ul class="bullets">
      <li>Domestic airfare</li>
      <li>Tips for the driver and guide</li>
    </ul>
    <p class="note" style="margin-top:22px">*Departure from Buffalo Airport (BUF) is also possible(transfer is not included in the program, and is an additional charge)</p>
    <p class="note">Participants can also return to New York, Manhattan, or JFK Airport (transfer is free). Departure from JFK airport is not possible on the 11th Day due to time constraints.</p>
    <p class="note">*We recommend extending your trip with additional nights in New York, for leisure time in Manhattan, Broadway shows, shopping, and much more.</p>
  </section>

  <section class="col col-days-a">
    <article class="day"><h3>Day 1</h3><p>Arrival to Washington, D.C., registration in hotel. Overnight in Washigton, D.C.</p></article>
    <article class="day"><h3>Day 2</h3><p>Sightseeing tour of Washington, D.C.: memorials, Capitol Bulding, White House, museums, and much more. Overnight in Washington, D.C.</p></article>
    <article class="day"><h3>Day 3</h3><p>Departure to Philadelphia. Sightseeing tour of Philadelphia. Departure to New York, leisure time in the evening. Overnight in New York</p></article>
    <article class="day"><h3>Day 4</h3><p>Sightseeing tour of New York: Manhattan, Wall Street, United Nations Building, Broadway, Times Square. <em>*optional cruise to the Statue of Liberty and Ellis Island. Overnight in New York</em></p></article>
    <article class="day"><h3>Day 5</h3><p>Departure to Boston. Sightseeing tour of Boston, Harvard University. Overnight in Boston</p></article>
  </section>

  <section class="col col-days-b">
    <article class="day"><h3>Day 6</h3><p>Departure to Montreal, sightseeing tour of the city. Overnight in Montreal</p></article>
    <article class="day"><h3>Day 7</h3><p>Sightseeing tour of Quebec, return to Montreal. Overnight in Montreal</p></article>
    <article class="day"><h3>Day 8</h3><p>Second part of sightseeing tour of Montreal. Old Town, Montreal Port, Notre Dame de Montreal. Departure to Ottawa, sightseeing tour of Ottawa. Overnight in Ottawa</p></article>
    <article class="day"><h3>Day 9</h3><p>Departure to Rockport, cruise of 1,000 Islands, Departure to Toronto. Overnight in Toronto</p></article>
    <article class="day"><h3>Day 10</h3><p>Sightseeing tour of Toronto. Departuure to Niagara Falls. Cruise to the Niagara Falls. Overnight in Niagara Falls</p></article>
    <article class="day"><h3>Day 11</h3><p>Transfer to Toronto Airport (YYZ). End of tour program</p></article>
  </section>

  <svg class="footer-art" width="949" height="135" viewBox="0 0 949 135" aria-hidden="true">
    <defs>
      <linearGradient id="slate" x1="0" y1="0" x2="0" y2="1">
        <stop offset="0" stop-color="#6a6a6a"/>
        <stop offset="1" stop-color="#3e3e3e"/>
      </linearGradient>
      <linearGradient id="crimson" x1="0" y1="0" x2="1" y2="0">
        <stop offset="0" stop-color="#d21c22"/>
        <stop offset="1" stop-color="#b3141a"/>
      </linearGradient>
    </defs>
    <path d="M0,42 C120,60 260,72 420,76 L378,135 H0Z" fill="url(#slate)"/>
    <path d="M398,135 L440,76 C650,68 840,50 949,18 V135Z" fill="url(#crimson)"/>
  </svg>

  <div class="fine fine-left">
    <p>**order of sights of interest may change with advance notice</p>
    <p>*Blue Pebble Trips, Inc. cannot be held liable for complications arising from improperly filled out forms, passports or visas, especially upon crossing international borders.</p>
  </div>
  <div class="fine fine-right">
    <p>* Blue Pebble Trips, Inc. cannot be held liable for forgotten personal belongings left in hotels, aboard the bus, or lost throughout the duration of the tour.</p>
  </div>

  <div class="contact address">
    <svg width="11" height="15" viewBox="0 0 11 15" style="margin-top:2px"><path d="M5.5,0 C2.5,0 0,2.4 0,5.4 C0,9.4 5.5,15 5.5,15 C5.5,15 11,9.4 11,5.4 C11,2.4 8.5,0 5.5,0Z" fill="var(--gold)"/><circle cx="5.5" cy="5.4" r="2" fill="#555"/></svg>
    <span>4150 Harbor View Ave. Suite #310<br>Marina Hills, CA 90212</span>
  </div>
  <div class="contact email">
    <svg width="18" height="13" viewBox="0 0 18 13"><rect x="1" y="1" width="16" height="11" fill="none" stroke="var(--gold)" stroke-width="1.6"/><path d="M1,1 L9,7.5 L17,1" fill="none" stroke="var(--gold)" stroke-width="1.6"/></svg>
    <span>info@bluepebbletrips.com</span>
  </div>
  <div class="contact phone">
    <svg width="22" height="22" viewBox="0 0 22 22"><circle cx="11" cy="11" r="10" fill="none" stroke="var(--gold)" stroke-width="1.6"/><path d="M7.5,6 L9.5,6 L10.3,8.6 L9,9.6 C9.7,11.1 10.9,12.3 12.4,13 L13.4,11.7 L16,12.5 L16,14.5 C12,15.2 6.8,10 7.5,6Z" fill="var(--gold)"/></svg>
    <span>+1 (800) 555-0142</span>
  </div>
  <div class="contact web">
    <svg width="15" height="15" viewBox="0 0 15 15"><g fill="none" stroke="var(--gold)" stroke-width="1.3"><circle cx="7.5" cy="7.5" r="6.5"/><ellipse cx="7.5" cy="7.5" rx="3" ry="6.5"/><path d="M1,7.5 H14 M2,4 H13 M2,11 H13"/></g></svg>
    <span>www.bluepebbletrips.com</span>
  </div>

</main>
</body>
</html>
```